Len Morvath

I am the director of Casa Del Humo International. We make premium cigars

I want an insanely beautiful card that directly attracts attention. Do your best. The card can use emboss, foil, laser-cut metal or anything else. Make it stand out, but also elegant.

Target Market(s)

Cigar Distributors

Industry/Entity Type

Cigars

Contact Information for Business Card

Email: len.morvath@morvaths.com + Logos (attached) + Position: Director + 'High-End Cigars'

Colors

Designer to choose colors to be used in the design.

Requirements
Nice to have
• Please check us out at www.casadelhumo.com and try to use our colors and styles

```html
<!DOCTYPE html>
<html lang="en">
<head>
<meta charset="utf-8">
<title>Casa Del Humo International – Business Card</title>
<link href="https://fonts.googleapis.com/css2?family=Cormorant+Garamond:wght@500;600&family=Playfair+Display:wght@500&family=Questrial&display=swap" rel="stylesheet">
<style>
  :root {
    --backdrop: #e8e8e9;
    --charcoal: #3b3a3a;
    --charcoal-shade: #333232;
    --card-red: #d4444c;
    --card-red-deep: #7c1a20;
    --ink-white: #f7f3f2;
    --serif: "Cormorant Garamond", Georgia, serif;
    --display: "Playfair Display", Georgia, serif;
    --sans: "Questrial", Arial, sans-serif;
  }
  * { box-sizing: border-box; margin: 0; padding: 0; }
  html, body {
    width: 1200px; height: 900px; overflow: hidden;
    background: var(--backdrop);
  }
  .canvas {
    width: 1200px; height: 900px;
    display: flex; flex-direction: column; align-items: center; justify-content: center;
    gap: 50px;
  }
  .card {
    position: relative;
    width: 640px; height: 366px;
    overflow: hidden;
    box-shadow: 0 10px 28px rgba(0,0,0,.16);
  }

  /* Front */
  .card--front {
    background: radial-gradient(ellipse at 40% 30%, var(--charcoal), var(--charcoal-shade));
    color: var(--ink-white);
  }
  .company-name {
    position: absolute; left: 0; right: 0; top: 160px;
    font-family: var(--serif);
    font-weight: 500;
    font-size: 28px;
    letter-spacing: 1px;
    line-height: 1.2;
    text-align: center;
  }
  .company-location {
    position: absolute; left: 0; right: 0; bottom: 34px;
    text-align: center;
    font-family: var(--sans);
    font-size: 12px;
    letter-spacing: 2px;
  }

  /* Back */
  .card--back {
    background: var(--card-red);
    color: var(--ink-white);
  }
  .back-block {
    position: absolute; left: 0; top: 0;
    width: 58%; height: 150px;
    background: var(--card-red-deep);
  }
  .back-rules { position: absolute; inset: 0; }
  .holder-name {
    position: absolute; left: 0; right: 0; top: 160px;
    text-align: center;
    font-family: var(--display);
    font-weight: 500;
    font-size: 36px;
    letter-spacing: 4px;
    line-height: 1;
  }
  .holder-role {
    position: absolute; left: 0; right: 0; top: 210px;
    text-align: center;
    font-family: var(--serif);
    font-weight: 600;
    font-size: 12px;
    line-height: 1;
  }
  .contact {
    position: absolute; left: 0; right: 0; top: 250px;
    text-align: center;
    font-family: var(--sans);
    font-size: 13.5px;
    line-height: 1.35;
  }
  .contact-email { margin-top: 10px; }
  .contact-email .label { font-weight: 700; margin-right: 14px; }
</style>
</head>
<body>
<main class="canvas">

  <section class="card card--front" aria-label="Card front">
    <h1 class="company-name">Casa Del Humo International</h1>
    <p class="company-location">VALLE ALTO - HONDURAS</p>
  </section>

  <section class="card card--back" aria-label="Card back">
    <div class="back-block"></div>
    <svg class="back-rules" width="640" height="366" viewBox="0 0 640 366" aria-hidden="true">
      <line x1="330" y1="204" x2="598" y2="204" stroke="var(--ink-white)" stroke-width="1.3"/>
      <line x1="60" y1="236" x2="400" y2="236" stroke="var(--ink-white)" stroke-width="1.3"/>
      <rect x="316" y="232" width="8" height="8" transform="rotate(45 320 236)" fill="var(--ink-white)"/>
    </svg>
    <h2 class="holder-name">Len Morvath</h2>
    <p class="holder-role">Director</p>
    <div class="contact">
      <p>4870, Barrio Las Palmas Calle Mayor,<br>Valle Alto, Honduras.</p>
      <p class="contact-email"><span class="label">E</span>len.morvath@morvaths.com</p>
    </div>
  </section>

</main>
</body>
</html>
```